Buy LumaPass landing page redesign

I would like the following page redesigned: http://luma-pass.co.uk/lpv3/signup.php
The header and footer will remain the same, but I need the content to be visually appealing.
The only requirements are the 3 card options - but the design of this can of course be completely different to what is currently there.
You can also use brand logos / names from our partner list - see http://luma-pass.co.uk/index.php or http://luma-pass.co.uk/partners for brands.
Happy to answer any questions or provide more detail, but essentially looking to make this page much more attractive in order to increase conversion - i.e. get people to buy a LumaPass
Target Market(s)
High income male and female audience
Font styles to use
Other font styles liked:
- Avenir
Colors
Designer to choose colors to be used in the design.
Requirements
Must have
- The current header and footer
The 3 card options (1 month, 6 months, 12 months)
Nice to have
- logos of partner brands could be used or else the animated gif that we currently have on the page
also the card graphics (mobile and card image) could be incorporated

```html
<!DOCTYPE html>
<html lang="en">
<head>
<meta charset="utf-8">
<title>Buy a LumaPass</title>
<link rel="stylesheet" href="https://fonts.googleapis.com/css2?family=Nunito+Sans:wght@300;400;600;700&family=Barlow+Condensed:wght@400;500;600&display=swap">
<style>
  :root {
    --ink: #111111;
    --paper: #ffffff;
    --nav-grey: #9a9a9a;
    --teal: #17a3c4;
    --pill-teal: #a6eef0;
    --pill-purple: #c9a6e8;
    --pill-yellow: #f6e69a;
    --card-grey: #dcdcdc;
    --card-edge: #c4c4c4;
    --button: #2e3236;
    --footer-text: #e8e8e8;
    --field: #ffffff;
    --field-dim: #d8d8d8;
    --body: "Nunito Sans", "Avenir", Arial, sans-serif;
    --condensed: "Barlow Condensed", "Arial Narrow", sans-serif;
  }
  * { box-sizing: border-box; margin: 0; padding: 0; }
  html, body { width: 796px; height: 1200px; overflow: hidden; background: var(--paper); }
  body { position: relative; font-family: var(--body); color: var(--ink); }
  .abs { position: absolute; }

  /* Header */
  .top-strip { left: 0; top: 0; width: 796px; height: 9px; background: var(--ink); }
  .account-tab { left: 554px; top: 9px; width: 214px; height: 20px; background: var(--ink); color: var(--paper);
    font-size: 8px; font-weight: 700; text-align: center; line-height: 20px; }
  .brand { left: 19px; top: 20px; font-size: 39px; font-weight: 400; letter-spacing: 1px; }
  .main-nav { left: 325px; top: 47px; display: flex; gap: 25px; font-size: 11px; color: var(--nav-grey); letter-spacing: .2px; }

  /* Hero */
  .hero { left: 0; top: 72px; width: 796px; height: 292px; }
  .hero-photo { left: 0; top: 0; width: 796px; height: 292px;
    background: linear-gradient(100deg, #e8c7a6 0%, #e2535a 18%, #f2d7c4 34%, #f7f3f6 52%, #ffffff 70%, #f2e6f7 86%, #d9b8ea 100%); }
  .hero-panel { left: 327px; top: 0; width: 463px; height: 292px; }
  .hero-rule { left: 0; top: 0; width: 463px; height: 3px; background: var(--ink); }
  .hero-title { left: 11px; top: 14px; font-size: 28px; font-weight: 400; }
  .hero-lead { left: 11px; top: 57px; font-family: var(--condensed); font-weight: 600; font-size: 19px; line-height: 1; }
  .hero-copy { left: 11px; top: 76px; width: 450px; font-size: 11px; line-height: 1.3; }
  .benefits-title { left: 70px; top: 124px; font-family: var(--condensed); font-weight: 600; font-size: 22px; color: var(--teal); }
  .benefits { left: 70px; top: 156px; list-style: none; font-size: 12px; }
  .benefits li { display: flex; align-items: center; gap: 10px; height: 24.4px; }
  .benefits svg { width: 16px; height: 14px; flex: none; }

  .section-rule { left: 16px; width: 755px; height: 4px; background: var(--ink); }

  /* Plans */
  .mascot { left: 31px; top: 442px; width: 234px; height: 208px;
    background: radial-gradient(ellipse at 55% 45%, #8a95a3 0%, #b8c2cc 38%, #ffffff 72%); border-radius: 40px; }
  .plan { top: 420px; width: 162px; height: 226px; border-radius: 6px;
    background: linear-gradient(180deg, #fafafa 0%, var(--card-grey) 100%);
    border: 3px solid var(--card-edge); }
  .plan-name { position: absolute; left: 9px; top: 9px; width: 141px; height: 30px; border-radius: 5px;
    font-size: 14px; text-align: center; line-height: 30px; }
  .plan-copy { position: absolute; left: 20px; top: 59px; width: 126px; font-size: 9px; line-height: 1.35; }
  .plan-price { position: absolute; left: 20px; top: 140px; font-size: 9px; line-height: 1.35; }
  .plan-buy { position: absolute; left: 30px; top: 178px; width: 102px; height: 26px; border-radius: 3px;
    background: var(--button); color: var(--paper); font-family: var(--condensed); font-weight: 600;
    font-size: 16px; text-align: center; line-height: 26px; letter-spacing: .3px; }

  .launch-note { left: 40px; top: 669px; width: 716px; text-align: center; font-family: var(--condensed);
    font-size: 23px; line-height: 1.28; }
  .intro { left: 100px; top: 766px; width: 540px; text-align: center; font-size: 56px; font-weight: 300;
    line-height: 1.22; letter-spacing: 1px; }

  /* Footer */
  .site-footer { left: 4px; top: 994px; width: 788px; height: 206px; background: var(--ink); color: var(--footer-text); font-size: 11px; }
  .signup-label { left: 46px; top: 24px; }
  .signup-form { left: 46px; top: 44px; display: flex; align-items: center; gap: 4px; }
  .field { height: 21px; background: var(--field); color: #999; font-size: 10px; padding: 4px 5px; }
  .field.email { width: 178px; }
  .field.code { width: 74px; height: 18px; background: var(--field-dim); margin-right: 10px; }
  .signup-btn { width: 52px; height: 18px; background: var(--field); color: #222; font-size: 10px; text-align: center; line-height: 18px; border-radius: 2px; }
  .connect-label { left: 537px; top: 24px; }
  .social { left: 540px; top: 39px; display: flex; gap: 8px; }
  .social span { width: 24px; height: 24px; background: var(--paper); display: block; }
  .footer-rule { left: 33px; top: 83px; width: 718px; height: 1px; background: #777; }
  .footer-links { top: 100px; list-style: none; line-height: 18.6px; }
  .legal { left: 372px; top: 100px; width: 380px; line-height: 18.6px; }
  .legal p + p { margin-top: 7px; }
</style>
</head>
<body>
  <header>
    <div class="abs top-strip"></div>
    <div class="abs account-tab">SIGN UP FOR DAILY EMAIL | LOGIN</div>
    <div class="abs brand">LUMAPASS</div>
    <nav class="abs main-nav">
      <span>WHAT IS LUMAPASS?</span><span>BUY A LUMAPASS</span><span>DAILY STORIES ▾</span><span>A-Z OF OFFERS</span>
    </nav>
  </header>

  <section class="abs hero">
    <div class="abs hero-photo" role="img" aria-label="Three smiling shoppers in sunglasses holding bags and a black LumaPass card towards the viewer"></div>
    <div class="abs hero-panel">
      <div class="abs hero-rule"></div>
      <h1 class="abs hero-title">Buy Your Luma Pass</h1>
      <p class="abs hero-lead">Buy a LumaPass and save on fashion, beauty, restaurants &amp; more</p>
      <p class="abs hero-copy">at all our partner brands each time you shop online or in-store. Start saving immediately by downloading your card straight to your mobile phone.</p>
      <h2 class="abs benefits-title">What you get with your LumaPass</h2>
      <ul class="abs benefits">
        <li><svg viewBox="0 0 16 14"><path d="M1 8l4 4L15 1" fill="none" stroke="#111" stroke-width="3"/></svg>Save on fashion, beauty, restaurants &amp; more</li>
        <li><svg viewBox="0 0 16 14"><path d="M1 8l4 4L15 1" fill="none" stroke="#111" stroke-width="3"/></svg>Digital LumaPass on your mobile phone</li>
        <li><svg viewBox="0 0 16 14"><path d="M1 8l4 4L15 1" fill="none" stroke="#111" stroke-width="3"/></svg>Notification of all new offers from brands</li>
        <li><svg viewBox="0 0 16 14"><path d="M1 8l4 4L15 1" fill="none" stroke="#111" stroke-width="3"/></svg>Optional weekly round-up</li>
        <li><svg viewBox="0 0 16 14"><path d="M1 8l4 4L15 1" fill="none" stroke="#111" stroke-width="3"/></svg>Reduced rate on LumaPass BLACK*</li>
      </ul>
    </div>
  </section>

  <div class="abs section-rule" style="top:366px"></div>

  <section>
    <div class="abs mascot" role="img" aria-label="Cartoon mobile phone walking along carrying a black LumaPass card"></div>

    <article class="abs plan" style="left:263px">
      <div class="plan-name" style="background:var(--pill-teal)">1 MONTH</div>
      <p class="plan-copy">A one month LumaPass is perfect ahead of a shopping spree. Whether you're buying gifts for friends, family or yourself, LumaPass is here to help.</p>
      <p class="plan-price">Price: <b>£4.99</b><br>For 1 Month</p>
      <div class="plan-buy">BUY NOW</div>
    </article>
    <article class="abs plan" style="left:433px">
      <div class="plan-name" style="background:var(--pill-purple)">6 MONTHS</div>
      <p class="plan-copy">Enjoy savings on fashion, beauty, restaurants and more for the next 6 months.</p>
      <p class="plan-price">Price: <b>£29.99</b><br>For 6 Months</p>
      <div class="plan-buy">BUY NOW</div>
    </article>
    <article class="abs plan" style="left:603px">
      <div class="plan-name" style="background:var(--pill-yellow)">12 MONTHS</div>
      <p class="plan-copy">Enjoy savings on fashion, beauty, restaurants and more for the next 12 months.</p>
      <p class="plan-price">Price: <b>£39.99</b><br>For 12 Months</p>
      <div class="plan-buy">BUY NOW</div>
    </article>

    <p class="abs launch-note">*LumaPass holders will be given an exclusive reduced rate upgrade option during the initial launch of the LumaPass BLACK</p>
  </section>

  <div class="abs section-rule" style="top:742px"></div>

  <h2 class="abs intro">INTRODUCING LUMAPASS</h2>

  <footer class="abs site-footer">
    <p class="abs signup-label">SIGN UP TO OUR DAILY EMAIL - Please enter the validation code: luma</p>
    <div class="abs signup-form">
      <span>Email:</span><span class="field email">enter your email address</span>
      <span>Code:</span><span class="field code">enter code</span>
      <span class="signup-btn">Sign up</span>
    </div>
    <p class="abs connect-label">CONNECT WITH LUMAPASS:</p>
    <div class="abs social" aria-label="Social links"><span></span><span></span><span></span><span></span><span></span><span></span><span></span></div>
    <div class="abs footer-rule"></div>
    <ul class="abs footer-links" style="left:46px"><li>About Us</li><li>Contact</li><li>Using Your Card</li><li>Buy A LumaPass</li><li>Become A Partner</li></ul>
    <ul class="abs footer-links" style="left:232px"><li>Shipping</li><li>Terms</li><li>Privacy Policy</li><li>Press</li><li>FAQs</li></ul>
    <div class="abs legal">
      <p>© LumaPass Ltd. All Rights Reserved.</p>
      <p>The celebrities named or featured on luma-pass.co.uk have not endorsed, recommended or approved the items featured on site.</p>
    </div>
  </footer>
</body>
</html>
```